High Profile Wordpress Design for Marketing Agency

http://www.VantaCom.co.nz is moving from DotNetNuke to wordpress

Vanta PR is a leading New Zealand consumer brands public relations and advertising agency.
Our marketing agency represents some of the worlds most recognisable brands as well as some small independent businesses and everything in between.
Our DNN current site has served us well for 6+ years but we are now wanting to move to wordpress.

We are looking for a new look for our website which will be either a 2013 facelift keeping existing colour scheme rather than a radical new design
Our target market is marketing managers and brand owners familiar with design and marketing elements.
First and foremost the site must be functional from an SEO and loading speed point of view. To assist this we want to retain the text content.
Secondly we have historically had only pointers to other pages on our site but we want to incorporate more of the highlights of our services and our portfolio with the addition of some 'sample boxes' such as in this template: http://layoutbazaar.example/item/sleek-firm-cms-theme/full_screen_preview/7305816

Wordpress offers an easier interface for uploading news items which we do daily and also take advantage of the plugins for seo. We are looking to redesign the look of the site while keeping all the existing text content.

Logo – also needs refreshing. Something corporate but not staid. Modern and clean.

Existing pages
- We want a fresh new clean look while retaining the orange and gray colours. white space is good. modern fonts are good.
- Social media : we want to focus on Google Plus primarily but also facebook and twitter. We suggest a funky design with the social media logos. Social media logos on all pages.
- Add New page: client coverage. A page to showcase new client coverage. Could be print, links to online video, mepgs, etc. Perhaps as a blog?
- Add New page: Advertising (as a service).

Home page. Perhaps a larger image existing image can be used or something new that says Stand out from the crowd (but not in a clichéd way). perhaps 3-4 main images could be used which rotate? We want to use stunning image(s) on the site.
Retain existing body of text somewhere on page.

an alternative idea might be to look at images which relate to news. and use the phrase "journalists reaching journalists"

Add Small ‘boxes’ on home page – teasers for content inside the site:
- Our clients logo box. Perhaps use a mouse over to ‘roll’ logos from homepage? Plus link to our clients page. http://www.vantacom.co.nz/OurClients/CurrentClients.aspx
- Our services
- Quotes about us. Show an image of Horizonte magazine with quote about us
- Advertising box: Featured project (as embedded youtube clip and link case study)
- Contact us page – refresh look simple details only.

Client News (blog) page:

Image(s) to top right rather than bottom.
Google Plus like one and share as first icon. Also facebook, twitter share and RSS. (moving icons which scroll down as reader moves down?)

Budget Increase to A$2190
Hi Budget on this project to redesign Auckland PR Firm Vanta PR's website in wordpress has been increased significantly to A$2190

Target Market(s)

Marketing managers, small - large business owners
we are primarily a public relations firm, then advertising. focus should be on these services rather than web design/seo etc which are a secondary part of our offering.

Industry/Entity Type

Advertising

Requirements
Must have
• must retain existing text content(for seo reasons)
fast loading, free of slow graphics
mobile/tablet friendly
new logo
Google Plus 1 logo
Should not have
• our agency is slightly on the conservative side and yet we are looking for a modern look.
prefer light over dark colour scheme/images
Images – better to not use people in images. people from stock images tend to give the impression of an international site and we are looking closer to NZ

```html
<!DOCTYPE html>
<html lang="en">
<head>
<meta charset="utf-8">
<title>Vanta PR – Home</title>
<link href="https://fonts.googleapis.com/css2?family=Ubuntu:wght@400;500;700&family=Quicksand:wght@300;400;500&family=Oswald:wght@300&family=Raleway:wght@200&display=swap" rel="stylesheet">
<style>
:root{
  --orange:#e8860c;
  --orange-dark:#c96f00;
  --ink:#1c1c1c;
  --body-text:#8a8a8a;
  --panel:#efefef;
  --band:#f3f2ef;
  --footer:#000000;
  --footer-text:#b5b5b5;
  --social:#d8161b;
  --client:#3a3a3a;
}
*{box-sizing:border-box;margin:0;padding:0}
html,body{width:743px;height:1200px;overflow:hidden;background:#fff}
body{font-family:"Ubuntu",Arial,sans-serif;color:var(--body-text)}
.canvas{position:relative;width:743px;height:1200px;overflow:hidden;background:#fff}
.abs{position:absolute}

/* header */
.site-header{left:0;top:0;width:743px;height:32px;background:linear-gradient(#fff,#f1f1f1)}
.brand{left:87px;top:6px;font-family:"Ubuntu",sans-serif;font-weight:500;font-size:18px;color:#5a5a5a}
.search{left:466px;top:7px;width:113px;height:19px;border:1px solid #cfcfcf;background:#fff;font-size:8px;color:#333;padding:4px 6px}
.search-btn{left:557px;top:8px;width:21px;height:17px;background:#444;border-radius:2px}
.login{left:590px;top:5px;width:62px;height:22px;background:var(--orange);border-radius:2px;color:#fff;font-weight:700;font-size:11px;padding:5px 0 0 22px}
.login svg{position:absolute;left:7px;top:4px}
.main-nav{left:0;top:32px;width:743px;height:27px;background:linear-gradient(#474747,#2c2c2c);display:flex;padding-left:87px}
.main-nav a{color:#fff;font-size:9.6px;text-decoration:none;padding:8px 6px 0;height:27px}
.main-nav a.active{background:var(--orange)}

/* hero */
.hero{left:0;top:60px;width:743px;height:255px;background:radial-gradient(ellipse at 40% 45%,#ffffff 0%,#f2f2f2 45%,#c9c9c9 100%)}
.hero-photo{left:105px;top:88px;width:300px;height:200px;background:linear-gradient(90deg,#dfe8d8,#c7d8bb 50%,#dfe6d8);border-radius:4px}
.hero-ring{left:352px;top:101px;width:225px;height:225px;border:1px solid #c8c8c8;border-radius:50%;border-right-color:transparent;border-bottom-color:transparent}
.hero-title{left:438px;top:141px;font-family:"Oswald",sans-serif;font-weight:300;font-size:49px;color:#111;line-height:1;letter-spacing:-0.5px}
.hero-sub{left:459px;top:198px;font-family:"Raleway",sans-serif;font-weight:200;font-size:20px;letter-spacing:4px;color:#333}
.social-tabs{left:713px;top:130px;width:30px}
.social-tabs span{display:block;width:30px;height:24px;margin-bottom:2px;background:var(--social);border-radius:3px 0 0 3px;position:relative}
.social-tabs span::after{content:"";position:absolute;left:10px;top:7px;width:10px;height:10px;border-radius:50%;background:#fff}

/* intro */
.section-title{font-family:"Quicksand",sans-serif;font-weight:300;color:var(--orange);font-size:21px}
.intro-title{left:96px;top:326px}
.col{width:178px;font-size:8.6px;line-height:12.1px;color:var(--body-text);letter-spacing:-0.1px}
.col p{margin-bottom:12.1px}
.col-left{left:98px;top:361px}
.col-mid{left:295px;top:361px}
.more-btn{background:var(--orange-dark);color:#fff;font-size:8px;font-weight:700;padding:3px 6px;border-radius:2px;display:inline-block}

/* sidebar */
.news-box{left:494px;top:332px;width:158px;height:224px;background:var(--panel)}
.news-title{position:absolute;left:8px;top:9px;color:var(--orange);font-weight:500;font-size:15px}
.news-item{position:absolute;left:7px;width:145px}
.news-date{position:absolute;left:0;top:0;width:30px;text-align:center;font-family:"Quicksand",sans-serif;color:#555;line-height:1}
.news-date b{display:block;font-weight:300;font-size:24px}
.news-date i{display:block;font-style:normal;font-weight:300;font-size:13px}
.news-head{position:absolute;left:41px;top:2px;font-size:8.5px;color:#222}
.news-body{position:absolute;left:41px;top:15px;width:105px;font-size:7.8px;line-height:10.4px;color:#999}
.quote-figure{left:494px;top:562px;width:62px;height:168px;background:linear-gradient(#f4f4f4,#3a3a3a 70%)}
.quote-card{left:494px;top:597px;width:158px;height:133px;background:linear-gradient(135deg,#f6a52a,#e07c06)}
.quote-text{left:598px;top:625px;width:52px;font-size:7.4px;line-height:9.4px;color:#fff}
.quote-mag{left:509px;top:685px;font-weight:700;font-size:17px;line-height:18px;color:#fff}

/* clients */
.client-rule{top:783px;height:1px;background:#ddd}
.client-title{left:326px;top:771px}
.client-row{left:88px;top:815px;width:568px;display:flex;justify-content:space-between;align-items:center}
.client-name{font-weight:500;font-size:12px;color:var(--client)}
.client-more{left:350px;top:858px;width:40px;height:14px;background:#bdbdbd;color:#fff;font-size:7.5px;font-weight:700;text-align:center;padding-top:3px;clip-path:polygon(15% 0,85% 0,100% 50%,85% 100%,15% 100%,0 50%)}

/* newsletter */
.signup{left:0;top:884px;width:743px;height:135px;background:var(--band)}
.signup-art{left:86px;top:902px;width:104px;height:100px;background:radial-gradient(circle at 55% 65%,#fbd25b,#f5b92c 40%,rgba(245,185,44,0) 70%)}
.signup-title{left:212px;top:907px;font-family:"Quicksand",sans-serif;font-weight:500;font-size:17px;color:var(--orange)}
.signup-sub{left:212px;top:926px;font-family:"Quicksand",sans-serif;font-weight:500;font-size:14px;color:#111}
.field{top:964px;width:156px;height:22px;border:1px solid #c9c9c9;background:#fff;font-size:9px;color:#555;padding:5px 6px}
.subscribe{left:538px;top:964px;width:81px;height:22px;background:#2e2e2e;color:#fff;font-weight:700;font-size:11px;text-align:center;padding-top:4px;border-radius:2px}

/* footer */
.site-footer{left:0;top:1019px;width:743px;height:152px;background:var(--footer)}
.foot-sep{top:1032px;width:1px;height:125px;background:#2a2a2a}
.foot-col{font-size:7.8px;color:var(--footer-text)}
.foot-col h4{font-weight:400;font-size:10px;color:var(--orange);margin-bottom:8px;text-transform:uppercase}
.foot-col li{list-style:none;line-height:9.5px;margin-bottom:8px;padding-left:6px;position:relative}
.foot-col li::before{content:"";position:absolute;left:0;top:3px;border-left:3px solid #888;border-top:2px solid transparent;border-bottom:2px solid transparent}
.copyright{left:0;top:1171px;width:743px;height:29px;background:var(--orange);color:#fff;font-size:7.5px;text-align:center;padding-top:7px}
</style>
</head>
<body>
<div class="canvas">

  <header class="site-header abs"></header>
  <div class="brand abs">Vanta PR</div>
  <div class="search abs">Search</div>
  <div class="search-btn abs">
    <svg width="21" height="17" viewBox="0 0 21 17"><circle cx="10" cy="7.5" r="3" fill="none" stroke="#fff" stroke-width="1.4"/><line x1="12.2" y1="9.7" x2="14.5" y2="12" stroke="#fff" stroke-width="1.6"/></svg>
  </div>
  <div class="login abs">
    <svg width="12" height="14" viewBox="0 0 12 14"><path d="M3 6V4a3 3 0 0 1 6 0v2" fill="none" stroke="#fff" stroke-width="1.6"/><rect x="1" y="6" width="10" height="8" rx="1" fill="#fff"/></svg>LOGIN
  </div>

  <nav class="main-nav abs">
    <a class="active">Home</a><a>Our Services</a><a>News</a><a>Our People</a><a>Advertising</a><a>Case Studies</a><a>Client Coverage</a><a>Our Clients</a><a>Contact Us</a>
  </nav>

  <section class="hero abs"></section>
  <div class="hero-photo abs" role="img" aria-label="Photo of a row of green chillies with a single red chilly standing out"></div>
  <div class="hero-ring abs"></div>
  <div class="hero-title abs">stand out</div>
  <div class="hero-sub abs">from the crowd</div>
  <div class="social-tabs abs" aria-label="Social links"><span></span><span></span><span></span><span></span></div>

  <h2 class="section-title intro-title abs">Who Are We</h2>
  <div class="col col-left abs">
    <p>Our experienced public relations specialists bring together a wealth of experience in public relations (PR), market research, magazines, FMCG / food and beverage marketing, television, and editorial journalism. We help our clients get closer to the mind of their target customer than they have ever been before.</p>
    <p>At Vanta PR, our marketing &amp; communications experts will work closely with you as your New Zealand public relations firm and if required, even as your advertising agency. Unlike many other public relations companies we also plan and buy media – however one of our key points of difference is our ability to enhance your brand equity by integrating your TV, print or digital marketing spend with an effective public relations strategy.</p>
    <p>Whether you are a small independent retailer or a large multinational corporation our Auckland PR agency has a solid branding solution for your budget.</p>
    <p>But don't just take our word for it; respected New Zealand business publication Horizonte magazine recently commented that Vanta PR's award winning director Mara Kestell provides "...the kind of external Public Relations expertise that small businesses are screaming out for...".</p>
  </div>
  <div class="col col-mid abs">
    <p>Our clients speak just as highly of us. Not just because we get outstanding results, not just because we offer great value for money, but because we listen.</p>
    <p>We listen to your marketing objectives, then our PR consultants design and construct a captivating public relations strategy to achieve these goals. Sometimes we work behind the scenes to achieve results on your behalf and sometimes we are recognised with our clients when industry accolades are awarded (as an example; taking out a 2012 MCANZ gold medal for marketing excellence).</p>
    <p>And, if one of those objectives is sales, we have introduced a new service allowing us to provide a virtual showroom and online retail outlet for our clients (such as Norvik car audio, Lumara cameras plus Corin Vale hair straighteners and hair dryers for those looking to create great hairstyles as well as Haldt electric shavers and Molarix electric toothbrushes), adventure cameras like the TrekCam HD Ridge2 cameras range, a line of Tavio T Force watches and now some new Trim Track NZ electronic scales - actually selling your products to an entirely new online market!</p>
    <span class="more-btn">MORE</span>
  </div>

  <aside class="news-box abs">
    <div class="news-title">Latest News</div>
    <div class="news-item" style="top:42px"><div class="news-date"><b>20</b><i>JAN</i></div><div class="news-head">Lorem ipsum dolor sit.</div><div class="news-body">Maecenas sollicitudin lorem in orci elementum nec semper lectus facilisis.</div></div>
    <div class="news-item" style="top:102px"><div class="news-date"><b>18</b><i>JAN</i></div><div class="news-head">Lorem ipsum dolor sit.</div><div class="news-body">Maecenas sollicitudin lorem in orci elementum nec semper lectus facilisis.</div></div>
    <div class="news-item" style="top:162px"><div class="news-date"><b>16</b><i>JAN</i></div><div class="news-head">Lorem ipsum dolor sit.</div><div class="news-body">Maecenas sollicitudin lorem in orci elementum nec semper lectus facilisis.</div></div>
  </aside>

  <div class="quote-card abs"></div>
  <div class="quote-figure abs" role="img" aria-label="Photo of a businessman shouting through a megaphone"></div>
  <div class="quote-text abs">"the kind of external PR expertise that small businesses are screaming out for ..."</div>
  <div class="quote-mag abs">HORIZONTE<br>MAGAZINE</div>

  <div class="client-rule abs" style="left:160px;width:160px"></div>
  <div class="client-rule abs" style="left:420px;width:160px"></div>
  <h2 class="section-title client-title abs">Our Client</h2>
  <div class="client-row abs">
    <span class="client-name">Corvetto</span>
    <span class="client-name">Harlan</span>
    <span class="client-name">Airlume</span>
    <span class="client-name">Fresca Home</span>
    <span class="client-name">Nuvela</span>
    <span class="client-name">Molarix</span>
    <span class="client-name">Velmira</span>
  </div>
  <div class="client-more abs">MORE</div>

  <section class="signup abs"></section>
  <div class="signup-art abs" role="img" aria-label="Illustration of a girl with a laptop riding a paper star"></div>
  <div class="signup-title abs">Keep in touch with our news and be the first one to know</div>
  <div class="signup-sub abs">don't worry! we won't spam you, we promise!</div>
  <div class="field abs" style="left:213px">Enter Your Name...</div>
  <div class="field abs" style="left:375px">Enter Your Email...</div>
  <div class="subscribe abs">SUBSCRIBE</div>

  <footer class="site-footer abs"></footer>
  <div class="foot-sep abs" style="left:162px"></div>
  <div class="foot-sep abs" style="left:362px"></div>
  <div class="foot-sep abs" style="left:453px"></div>
  <div class="foot-col abs" style="left:87px;top:1035px"><h4>Quick Link's</h4><ul><li>Home</li><li>About Us</li><li>Services</li><li>News</li><li>Coaches</li></ul></div>
  <div class="foot-col abs" style="left:173px;top:1035px"><h4>Our Services</h4><ul><li>Public Relations</li><li>Advertising</li><li>Media Training</li><li>Social Media</li><li>Online Reputation<br>Management</li></ul></div>
  <div class="foot-col abs" style="left:262px;top:1053px"><ul><li>Celebrity Appearances</li><li>Copywriting</li><li>Events</li><li>SEO</li><li>Web Design</li></ul></div>
  <div class="foot-col abs" style="left:374px;top:1035px"><h4>News</h4><ul><li>Client News</li><li>Vanta PR News</li></ul></div>
  <div class="foot-col abs" style="left:374px;top:1093px"><h4>Our Clients</h4><ul><li>Current Clients</li><li>Past Clients</li></ul></div>
  <div class="foot-col abs" style="left:467px;top:1035px"><h4>Case Studies</h4><ul><li>SkinScan Australasia</li><li>Zip Tablet</li><li>Yardmark</li><li>Vodka Brand Launch</li><li>budgetcoach.example</li></ul></div>
  <div class="foot-col abs" style="left:558px;top:1053px"><ul><li>Kauri Lodge Rotorua</li><li>Kiwi Air Fashion Week</li><li>The Painted Compass</li><li>Rowan Ellis</li></ul></div>
  <div class="copyright abs">©2013 &nbsp;Vanta PR Limited</div>

</div>
</body>
</html>
```